Business Card Design Project

1. Show the company logo.
2. Only company email ID and website address to be shown (office@zolotoyveter.fm , www.zolotoyveter.fm).
3. Logo to be provided by us, 2 designs just in case. The logo is made with ' Zolotoy Veter' text, need to be edited so that it shows 'Tikhaya Gavan' instead .
4. Single sided business card, portrait or landscape is not a problem; back side to be filled with colors or a design that matches the logo the best.
5. Logo is to be embossed.
6. We're looking at an English and Russian version.
7. any other better idea is always welcomed.

```html
<!DOCTYPE html>
<html lang="en">
<head>
<meta charset="utf-8">
<title>Business Card Design — Zolotoy Veter</title>
<link href="https://fonts.googleapis.com/css2?family=Arimo:wght@400;700&family=Oswald:wght@300&display=swap" rel="stylesheet">
<style>
  :root {
    --board-light: #f1f1f1;
    --board-dark: #c9c9c9;
    --card: #ffffff;
    --band: #2a2625;
    --band-edge: #403b39;
    --gold: #f2b600;
    --logo-blue: #143f86;
    --link-blue: #0f57a8;
    --back-blue: #1d8fd8;
    --icon-bg: #3a3a3c;
    --icon-blue: #23a3e6;
    --muted: #6a6a6a;
    --title-grey: #8a8a8a;
    --title-slate: #4a5069;
    --title-dark: #1c1c20;
    --rule: #9a9a9a;
  }
  * { box-sizing: border-box; margin: 0; padding: 0; }
  html, body { width: 1200px; height: 846px; overflow: hidden; }
  body {
    position: relative;
    background: radial-gradient(ellipse at 35% 30%, var(--board-light) 0%, #e2e2e2 55%, var(--board-dark) 100%);
    font-family: "Arimo", Arial, sans-serif;
  }
  .card {
    position: absolute;
    width: 508px;
    height: 290px;
    background: var(--card);
    box-shadow: 6px 8px 12px rgba(0,0,0,0.35);
    overflow: hidden;
  }
  .card--front-en { left: 80px; top: 100px; }
  .card--front-ru { left: 640px; top: 100px; }
  .card--back { left: 80px; top: 454px; }

  .band {
    position: absolute;
    left: 0; right: 0;
    height: 66px;
    background: linear-gradient(to bottom, var(--band-edge), var(--band) 40%, var(--band) 80%, #1b1817);
    border-top: 2px solid var(--gold);
    border-bottom: 2px solid var(--gold);
  }
  .card--front-en .band, .card--front-ru .band { top: 96px; }
  .card--back .band { top: 95px; }

  .logo-mark {
    position: absolute;
    left: 52px; top: 38px;
    width: 182px; height: 182px;
    border-radius: 50%;
    background: var(--logo-blue);
    box-shadow: 0 2px 6px rgba(0,0,0,0.3);
    display: flex;
    align-items: center;
    justify-content: center;
  }
  .logo-name {
    color: #ffffff;
    font-weight: 700;
    font-size: 17px;
    line-height: 1.15;
    text-align: center;
  }

  .player {
    position: absolute;
    left: 267px; top: 113px;
    display: flex;
    align-items: center;
    gap: 14px;
  }
  .player__btn {
    width: 38px; height: 32px;
    background: var(--icon-bg);
    border-radius: 3px;
    display: flex; align-items: center; justify-content: center;
  }
  .player__slider { width: 48px; height: 10px; margin-left: -8px; }

  .contact { position: absolute; left: 268px; top: 174px; }
  .contact__web { color: var(--link-blue); font-weight: 700; font-size: 16px; }
  .contact__mail { color: var(--muted); font-size: 13px; margin-top: 5px; }

  .back__web {
    position: absolute;
    left: 56px; top: 24px;
    color: var(--back-blue);
    font-weight: 700;
    font-size: 14px;
  }

  .caption {
    position: absolute;
    left: 641px; top: 454px;
    width: 320px;
    font-family: "Oswald", "Arial Narrow", sans-serif;
    font-weight: 300;
  }
  .caption__type { font-size: 37px; color: var(--title-grey); padding-left: 6px; line-height: 1.2; }
  .caption__rule { height: 2px; background: var(--rule); margin-top: 18px; }
  .caption__label { font-size: 29px; color: var(--title-slate); padding-left: 6px; margin-top: 12px; line-height: 1.2; }
  .caption__label small { font-size: 21px; color: var(--title-grey); margin-left: 6px; }
  .caption__client { font-size: 44px; color: var(--title-dark); padding-left: 6px; line-height: 1.15; letter-spacing: 0.5px; }
  .caption__rule--bottom { margin-top: 10px; }
</style>
</head>
<body>

  <article class="card card--front-en">
    <div class="band"></div>
    <div class="logo-mark"><span class="logo-name">Zolotoy<br>Veter</span></div>
    <div class="player">
      <div class="player__btn">
        <svg width="22" height="16" viewBox="0 0 22 16"><polygon points="1,1 10,8 1,15" fill="var(--icon-blue)"/><rect x="12" y="1" width="3" height="14" fill="var(--icon-blue)"/><rect x="17" y="1" width="3" height="14" fill="var(--icon-blue)"/></svg>
      </div>
      <div class="player__btn">
        <svg width="22" height="18" viewBox="0 0 22 18"><polygon points="1,6 5,6 10,1 10,17 5,12 1,12" fill="var(--icon-blue)"/><path d="M13 5 Q16 9 13 13 M16 3 Q20 9 16 15" stroke="var(--icon-blue)" stroke-width="1.6" fill="none"/></svg>
      </div>
      <svg class="player__slider" viewBox="0 0 48 10"><rect x="0" y="4" width="44" height="2" fill="#555"/><rect x="40" y="1" width="4" height="8" fill="#bbb"/></svg>
    </div>
    <div class="contact">
      <p class="contact__web">www.zolotoyveter.fm</p>
      <p class="contact__mail">office@zolotoyveter.fm</p>
    </div>
  </article>

  <article class="card card--front-ru">
    <div class="band"></div>
    <div class="logo-mark"><span class="logo-name">Tikhaya<br>Gavan</span></div>
    <div class="player">
      <div class="player__btn">
        <svg width="22" height="16" viewBox="0 0 22 16"><polygon points="1,1 10,8 1,15" fill="var(--icon-blue)"/><rect x="12" y="1" width="3" height="14" fill="var(--icon-blue)"/><rect x="17" y="1" width="3" height="14" fill="var(--icon-blue)"/></svg>
      </div>
      <div class="player__btn">
        <svg width="22" height="18" viewBox="0 0 22 18"><polygon points="1,6 5,6 10,1 10,17 5,12 1,12" fill="var(--icon-blue)"/><path d="M13 5 Q16 9 13 13 M16 3 Q20 9 16 15" stroke="var(--icon-blue)" stroke-width="1.6" fill="none"/></svg>
      </div>
      <svg class="player__slider" viewBox="0 0 48 10"><rect x="0" y="4" width="44" height="2" fill="#555"/><rect x="40" y="1" width="4" height="8" fill="#bbb"/></svg>
    </div>
    <div class="contact">
      <p class="contact__web">www.zolotoyveter.fm</p>
      <p class="contact__mail">office@zolotoyveter.fm</p>
    </div>
  </article>

  <article class="card card--back">
    <div class="band"><p class="back__web">www.zolotoyveter.fm</p></div>
  </article>

  <section class="caption">
    <p class="caption__type">Type A</p>
    <div class="caption__rule"></div>
    <p class="caption__label">Business Card Design<small>for</small></p>
    <p class="caption__client">ZOLOTOY VETER</p>
    <div class="caption__rule caption__rule--bottom"></div>
  </section>

</body>
</html>
```